I need a book cover design for my book "Scarlet Brambles." It is a non-fiction book focused on answering the question of whether American evangelicals look more like the Pharisees than Jesus.

The subtitle is "The Quiet Parallels of Modern Suburban Townsfolk and an Ancient Kingdom's Proud Rulers." The author name is Colin Marwood.

I will be publishing this as an ebook and paperback.

I am open to all ideas, but will share the only thought I had as a possible design. In the title, the third letter in both words is "A." I thought about the idea of having the "A" in "Evangelical" have a halo and the "A" in "Pharisees" somehow seem to be a shadow of that first "A" but have devil horns instead of a halo. Again, I'm not sold on that, but am sharing it as one design possibility.

I am not interested in the book cover design having a cheesy religious look to it (as many do). I am more interested in it looking like a professional non-fiction cover.

```html
<!DOCTYPE html>
<html lang="en">
<head>
<meta charset="utf-8">
<title>Scarlet Brambles — Book Cover</title>
<link rel="stylesheet" href="https://fonts.googleapis.com/css2?family=Princess+Sofia&family=Dancing+Script:wght@500&family=Open+Sans:wght@700&display=swap">
<style>
  :root {
    --page-bg: #141110;
    --paint-ember: #e9813c;
    --paint-scarlet: #b9352f;
    --paint-wine: #6f2a3c;
    --paint-plum: #4a2a55;
    --paint-night: #241828;
    --paint-ice: #5fb4cf;
    --paint-mauve: #9a6c78;
    --paint-slate: #6f7fa8;
    --title-gold: #f2d29a;
    --author-cream: #fff0d6;
    --subtitle-white: #ffffff;
  }
  * { margin: 0; padding: 0; box-sizing: border-box; }
  html, body {
    width: 1200px;
    height: 1120px;
    overflow: hidden;
    background: var(--page-bg);
  }
  .canvas {
    position: relative;
    width: 1200px;
    height: 1120px;
  }
  .book-cover {
    position: absolute;
    left: 252px;
    top: 40px;
    width: 696px;
    height: 1040px;
    overflow: hidden;
  }
  .cover-background {
    position: absolute;
    inset: 0;
    background:
      radial-gradient(ellipse 42% 20% at 8% 3%, var(--paint-ember) 0%, transparent 75%),
      radial-gradient(ellipse 45% 40% at 78% 42%, var(--paint-scarlet) 0%, transparent 75%),
      linear-gradient(165deg, var(--paint-wine) 0%, var(--paint-plum) 50%, var(--paint-night) 100%);
  }
  .cover-portrait {
    position: absolute;
    left: 30px;
    top: 120px;
    width: 440px;
    height: 920px;
    border-radius: 55% 45% 20% 30% / 30% 28% 0 0;
    background:
      radial-gradient(ellipse 38% 22% at 52% 30%, var(--paint-ice) 0%, transparent 80%),
      radial-gradient(ellipse 60% 40% at 45% 50%, var(--paint-mauve) 0%, transparent 85%),
      linear-gradient(180deg, #8a4a4e 0%, var(--paint-mauve) 40%, var(--paint-slate) 75%, #3c2d4a 100%);
    box-shadow: 0 0 60px 20px rgba(36, 24, 40, 0.35);
  }
  .cover-title {
    position: absolute;
    left: 282px;
    top: 40px;
    font-family: "Princess Sofia", cursive;
    font-weight: 400;
    font-size: 74px;
    line-height: 1.05;
    color: var(--title-gold);
  }
  .cover-title .title-line { display: block; }
  .cover-title .title-line--second { padding-left: 44px; }
  .cover-author {
    position: absolute;
    left: 414px;
    top: 255px;
    font-family: "Dancing Script", cursive;
    font-weight: 500;
    font-size: 26px;
    color: var(--author-cream);
  }
  .cover-subtitle {
    position: absolute;
    left: 0;
    right: 0;
    top: 953px;
    text-align: center;
    font-family: "Open Sans", sans-serif;
    font-weight: 700;
    font-size: 18px;
    line-height: 1.75;
    text-transform: uppercase;
    color: var(--subtitle-white);
  }
</style>
</head>
<body>
  <main class="canvas">
    <section class="book-cover">
      <div class="cover-background"></div>
      <div class="cover-portrait" role="img" aria-label="Painted portrait in profile, head tilted upward with eyes closed, lit in icy blue against ember, scarlet and plum brushstrokes"></div>
      <h1 class="cover-title">
        <span class="title-line">Scarlet</span>
        <span class="title-line title-line--second">Brambles</span>
      </h1>
      <p class="cover-author">Colin Marwood</p>
      <p class="cover-subtitle">The Quiet Parallels of Modern Suburban Townsfolk<br>and an Ancient Kingdom's Proud Rulers</p>
    </section>
  </main>
</body>
</html>
```